Mirna chewable tablets 3 panel sticker/template for tablet line - sticker die line is attached.

Sticker design for our line of chewable THC tablets. Product name is "Verdelles" We have 4 flavor varieties of tablets - Matcha Peppermint, Ginger, Lavender Pomegranate, & Lemon Chiffon. Please design the basic peel and reveal label, that will be easy to change just colors and a few details on to designate each formula. see inspiration photo attached.

(B in mirna is lower case.) Please also see other product packaging within our line, to coordinate your design with. Thanks! ;-) All compliance fonts must be 1/16th" or larger.

Target Market(s)

21+ professional women and/or men, looking for lower dose THC products - more functional products, to help with sleep, anxiety, pain, inflammation and just relaxing/recharging.

Industry/Entity Type

Cannabis

Font styles to use
Serif
Other font styles liked:
• See attached packaging to match font & coordinate look with.

Requirements
Must have
• This design includes 3 panels, as this is peel and reveal sticker that fits on a small box that slides to open. View box here: https://plovikbox.com/packaging/tornaglide/

Needs a peel back suggestion, so people know to open the sticker.

All compliance language must be at least 1/16" font size.

Panel 1 is the marketing layer must have the THC logo and the following warning statement "CONTAINS MARIJUANA. KEEP AWAY FROM CHILDREN." This warning statement must be directly below the THC logo - see attachment for THC icon/logo. Icon/THC logo must be 1/2" in size on final sticker and in red, exactly as shown in attachment this font must be 1/16"

Product name: Verdelles or Verdelles by Mirna (perhaps incorporate our logo with the flower?)
SKU specific details: Ginger, 3 mg THC, 10 mg CBD, 3 mg CBG. 30 fast acting chewable tablets.
Please also try to incorporate the pattern that is attached on this panel, that is carried over from our other products in this line. Colors can shift to match flavor. (Note, this packaging does not need the water color design or floral icon additions like other packaging has), the windowpane design is enough carry over.

Since this is such a small surface, let's keep it pretty clean and simple.

This outside panel/marketing layer of the sticker will be silver backed, so feel free to incorporate that to show through in the design if possible.

Middle section panel of the sticker will list ingredients:

Ginger, sugar, maltodextrin, magnesium stearate, microcrystalline cellulose, dicalcium phosphate, silicon dioxide, and food grade colorant, hemp derived CBD and CBG, cannabis derived THC.

Also on this ingredient panel or regulatory language panel, please have a product facts box containing this:

Serving size 1 tablet = 3 mg THC, 10 mg CBD, 3 mg CBG
Total cannabinoids per package 90 mg THC, 300 mg CBD, 90 mg CBG.
480 mg total cannabinoids. Total net weight: 10.5 g

www.mirnaolev.com
Store in a cool dry place.

(This ingredient panel will change slightly with each SKU, so it needs to be editable as we create new SKUs. panels 2 & 3 can be black and white since it is just text.)

Final panel should be this compliance language:

THIS PRODUCT WAS PRODUCED WITHOUT REGULATORY OVERSIGHT FOR HEALTH, SAFETY, OR EFFICACY. THERE MAY BE LONG TERM PHYSICAL OR MENTAL HEALTH RISKS FOR USE OF MARIJUANA INCLUDING ADDITIONAL RISKS FOR WOMEN WHO ARE OR MAY BE PREGNANT OR ARE BREASTFEEDING. USE OF MARIJUANA MAY IMPAIR YOUR ABILITY TO DRIVE A CAR OR OPERATE MACHINERY. THE INTOXICATING EFFECTS OF THIS PRODUCT MAY BE DELAYED BY UP TO 4 HOURS.
Should not have
• No pot leaves or typical stoner representations.

```html
<!DOCTYPE html>
<html lang="en">
<head>
<meta charset="utf-8">
<title>Verdelles by Mirna – Ginger label panels</title>
<link rel="stylesheet" href="https://fonts.googleapis.com/css2?family=Raleway:ital,wght@0,300;0,400;0,500;0,600;0,700;1,400&family=Cinzel:wght@700&display=swap">
<style>
  :root {
    --backdrop: #fbe3ec;
    --panel: #ffffff;
    --panel-shadow: #e46fae;
    --ink: #231f20;
    --accent: #d63f9a;
  }
  * { box-sizing: border-box; margin: 0; padding: 0; }
  html, body { width: 1200px; height: 900px; overflow: hidden; }
  body {
    background: var(--backdrop);
    font-family: "Raleway", sans-serif;
    color: var(--ink);
    position: relative;
  }
  .panel {
    position: absolute;
    left: 262px;
    width: 664px;
    background: var(--panel);
    border-radius: 24px;
    box-shadow: 4px 5px 0 0 var(--panel-shadow), 6px 8px 14px rgba(214, 63, 154, 0.25);
  }
  .panel--ingredients { top: 94px; height: 305px; }
  .panel--compliance { top: 487px; height: 305px; }

  .facts {
    position: absolute;
    left: 28px; top: 28px;
    width: 282px; height: 217px;
    border: 1px solid var(--ink);
    padding: 6px 10px 0 11px;
    font-size: 13px;
  }
  .facts__title { font-weight: 700; font-size: 16px; line-height: 20px; }
  .facts__serving { font-size: 13px; line-height: 15px; margin-bottom: 6px; }
  .facts__rule-thick { height: 5px; background: var(--ink); margin: 0 0 4px 0; }
  .facts__rule { height: 2px; background: var(--ink); margin-top: 4px; }
  .facts__head, .facts__row { display: grid; grid-template-columns: 52px 1fr 36px; }
  .facts__head { font-size: 13px; padding-top: 2px; }
  .facts__head span:nth-child(2) { padding-left: 2px; }
  .facts__rows { padding: 8px 0 4px; }
  .facts__row { font-size: 15px; line-height: 20px; }
  .facts__row span:nth-child(2) { padding-left: 49px; }
  .facts__row span:last-child, .facts__head span:last-child { text-align: right; padding-right: 2px; }
  .facts__note { font-size: 13px; line-height: 16px; padding: 6px 0 0 3px; }
  .facts__note + .facts__note { padding-top: 4px; }

  .net-weight {
    position: absolute;
    left: 180px; top: 262px;
    font-family: "Cinzel", serif;
    font-weight: 700;
    font-size: 12px;
    letter-spacing: 0.5px;
  }

  .details { position: absolute; left: 336px; top: 25px; width: 240px; font-size: 13px; line-height: 17px; }
  .details strong { font-weight: 700; }
  .details__totals { margin: 22px 0 0 3px; }
  .details__storage { margin: 16px 0 0 3px; font-style: italic; font-size: 15px; }
  .details__web { margin: 16px 0 0 3px; color: var(--accent); font-weight: 600; font-size: 15px; }

  .warning {
    position: absolute;
    left: 108px; top: 50px;
    width: 520px;
    font-size: 15.5px;
    line-height: 25.6px;
    letter-spacing: 0.3px;
    text-transform: uppercase;
  }
</style>
</head>
<body>
  <section class="panel panel--ingredients">
    <div class="facts">
      <h2 class="facts__title">Product Facts</h2>
      <p class="facts__serving">Serving size 1 tablet</p>
      <div class="facts__rule-thick"></div>
      <div class="facts__head"><span></span><span>Amount per Serving</span><span>%DV</span></div>
      <div class="facts__rule"></div>
      <div class="facts__rows">
        <div class="facts__row"><span>THC</span><span>3 mg</span><span>†</span></div>
        <div class="facts__row"><span>CBD</span><span>10 mg</span><span>†</span></div>
        <div class="facts__row"><span>CBG</span><span>3 mg</span><span>†</span></div>
      </div>
      <div class="facts__rule-thick" style="margin:0"></div>
      <p class="facts__note">% &nbsp;Daily Value are based on a 2,000 calorie diet</p>
      <p class="facts__note">† &nbsp;Daily value not establish</p>
    </div>
    <p class="net-weight">NET WEIGHT: 10.5 G</p>

    <div class="details">
      <p><strong>Ingredients:</strong> Ginger, sugar, maltodextrin, magnesium stearate, microcrystalline cellulose, dicalcium phosphate, silicon dioxide, and food grade colorant, hemp derived CBD and CBG, Marijuana derived THC.</p>
      <p class="details__totals">Total cannabinoids per package 90 mg THC, 300 mg CBD, 90 mg CBG. 480 mg total cannabinoids.</p>
      <p class="details__storage">Store in a cool dry place.</p>
      <p class="details__web">www.mirnaolev.com</p>
    </div>
  </section>

  <section class="panel panel--compliance">
    <p class="warning">This product was produced without regulatory oversight for health, safety, or efficacy. There may be long term physical or mental health risks for use of marijuana including additional risks for women who are or may be pregnant or are breastfeeding. Use of marijuana may impair your ability to drive a car or operate machinery. The intoxicating effects of this product may be delayed by up to 4 hours.</p>
  </section>
</body>
</html>
```